INNOVATION WEBSITE NEEDED: Agency from NZ needs YOU

Please see the enclosed documents for a detailed brief. It needs to be clean / simple / elegant / premium looking - that will appeal to companies that range from start-up to multi-national!
Note:
Perhaps instead of an actual shop, people can press an 'enquire now' button?

Target Market(s)

Start ups to multi-nationals

Industry/Entity Type

Marketing

Number of Pages Required

5+ page

Requirements
Must have
• Wordpress
• SEO
• Format friendly (mobile / tablet / etc)
• I have the URL: www.qu-tessaroly.com - I would like a working website. Please let me know what else you require to 'go live' with. Thanks!
Nice to have
• Please use / improve on my current ideas
• Perhaps use my logo icon (in different colours) for each 'product'?

```html
<!DOCTYPE html>
<html lang="en">
<head>
<meta charset="utf-8">
<title>Qu-Tessaroly — Creating the Future</title>
<link rel="stylesheet" href="https://fonts.googleapis.com/css2?family=Cinzel:wght@400;600;700&family=Lato:wght@400;700&display=swap">
<style>
:root{
  --navy:#24205e;
  --sky:#1ea8e8;
  --sky-soft:#5cc6f2;
  --pale:#dbe3f3;
  --green:#6aa84f;
  --ink:#333;
  --wood-a:#e9dcc6;
  --wood-b:#f3ead9;
  --white:#fff;
  --rule:#cfd3dc;
}
*{box-sizing:border-box;margin:0;padding:0}
html,body{width:1200px;height:2703px;overflow:hidden;background:var(--white)}
body{position:relative;font-family:"Lato",Arial,sans-serif;color:var(--ink)}
.abs{position:absolute}
.serif{font-family:"Cinzel",Georgia,serif}

/* hero */
.hero{position:absolute;left:0;top:0;width:1200px;height:607px;background:linear-gradient(100deg,var(--wood-a),var(--wood-b) 55%,var(--wood-a))}
.brand{position:absolute;left:99px;top:56px;display:flex;align-items:center;gap:14px}
.brand-dot{width:46px;height:46px;border-radius:50%;background:var(--navy)}
.brand-name{font-family:"Cinzel",Georgia,serif;font-size:30px;font-weight:700;color:var(--navy);line-height:1}
.topbar{position:absolute;right:88px;top:18px;display:flex;align-items:center;gap:14px}
.phone{display:flex;align-items:center;gap:8px;font-weight:700;font-size:17px;color:#222;margin-right:14px}
.social{width:30px;height:30px;border-radius:50%;background:#5d5d5d}
.nav{position:absolute;left:450px;top:78px;display:flex;list-style:none}
.nav li{font-family:"Cinzel",Georgia,serif;font-size:16px;color:var(--navy);padding:6px 14px;border-left:1px solid #b9ab95}
.nav li:first-child{border-left:none}
.nav .active{border:1.5px solid var(--navy);padding:5px 12px}
.book{position:absolute;left:27px;top:198px;width:523px;height:342px;border-radius:6px;background:linear-gradient(160deg,#d6d8dc,#a9acb3)}
.hero-copy{position:absolute;right:88px;top:214px;text-align:right}
.hero-copy h1{font-family:"Cinzel",Georgia,serif;font-size:35px;font-weight:700;line-height:44px;color:#1e1e1e}
.btn-buy-hero{display:inline-block;margin-top:20px;background:var(--navy);color:var(--white);font-weight:700;font-size:23px;padding:6px 18px;border-radius:4px}
.hero-copy .offer{margin-top:14px;font-weight:700;font-size:22px;line-height:33px;color:#1e1e1e}
.dots{position:absolute;left:1045px;top:522px;display:flex;gap:5px}
.dots span{width:11px;height:11px;border-radius:50%;background:#6b6b6b}
.dots span:first-child{background:var(--navy)}

/* welcome */
.welcome{position:absolute;top:607px;left:0;width:1200px;height:351px;text-align:center}
.welcome h2{position:absolute;left:0;right:0;top:53px;font-family:"Cinzel",Georgia,serif;font-size:33px;font-weight:600;color:#1e1e1e;display:flex;justify-content:center;align-items:center;gap:16px}
.welcome h2 em{font-style:normal;color:var(--navy)}
.welcome h2 i{width:34px;height:34px;border-radius:50%;background:var(--navy);display:inline-block}
.welcome p{position:absolute;left:108px;width:991px;top:146px;font-size:12.5px;line-height:20px;color:#444}
.btn-outline{display:inline-block;border:1.5px solid var(--navy);color:var(--navy);font-size:15px;font-weight:700;padding:8px 0;width:134px;text-align:center;background:var(--white)}
.welcome .btn-outline{position:absolute;left:533px;top:263px}

/* features */
.features{position:absolute;top:958px;left:0;width:1200px;height:469px;background:var(--pale)}
.feature{position:absolute;top:0;width:420px;text-align:center}
.feature svg{margin-top:33px}
.feature h3{font-family:"Cinzel",Georgia,serif;font-size:28px;font-weight:600;color:var(--navy);margin-top:20px}
.feature .lead{font-size:19px;font-weight:700;line-height:29px;color:#2a2a2a;margin-top:14px}
.feature ul{list-style:none;text-align:center;margin-top:12px}
.feature li{font-size:15px;line-height:21px;color:#333;margin-bottom:12px;padding:0 40px}
.feature li::before{content:"";display:inline-block;width:8px;height:8px;border-radius:50%;background:var(--sky);margin-right:8px;vertical-align:2px}
.feature .body{font-size:15px;line-height:23px;color:#333;margin-top:14px;padding:0 18px}
.feature .btn-outline{position:absolute;left:143px;top:404px}
.feature-what{left:55px}
.feature-purpose{left:743px}

/* how it works */
.how{position:absolute;top:1427px;left:0;width:1200px;height:479px}
.section-title{position:absolute;left:0;right:0;text-align:center;font-family:"Cinzel",Georgia,serif;font-size:34px;font-weight:600;color:#1e1e1e}
.divider{position:absolute;left:412px;width:376px;height:20px}
.how .section-title{top:53px}
.how .divider{top:110px}
.how svg.steps{position:absolute;left:0;top:160px}
.step-label{position:absolute;width:200px;text-align:center;font-family:"Cinzel",Georgia,serif;font-size:16px;line-height:25px;color:var(--navy);font-weight:600}

/* shop */
.shop{position:absolute;top:1906px;left:0;width:1200px;height:472px;background:var(--pale)}
.shop .section-title{top:48px}
.shop .divider{top:104px}
.product{position:absolute;top:166px;width:200px;text-align:center}
.product-icon{width:96px;height:96px;border-radius:50%;margin:0 auto;border:9px solid var(--sky-soft);background:var(--white);display:flex;align-items:center;justify-content:center}
.product-icon span{width:46px;height:46px;border-radius:50%;background:var(--navy)}
.product h4{font-family:"Cinzel",Georgia,serif;font-size:19px;font-weight:600;color:#222;margin-top:42px}
.product .price{font-size:21px;font-weight:700;color:#333;margin-top:8px}
.product .price.featured{color:#3a6fb5}
.btn-buy{display:block;margin:14px auto 0;width:119px;padding:8px 0;background:var(--green);color:var(--white);font-weight:700;font-size:17px;border:1.5px solid #4d8a35}

/* footer */
.footer{position:absolute;top:2378px;left:0;width:1200px;height:282px;background:var(--navy);color:var(--white)}
.fcol{position:absolute;top:40px}
.fcol h5{font-family:"Cinzel",Georgia,serif;font-size:17px;font-weight:400;padding-bottom:10px;border-bottom:1px solid #4b4787;width:160px}
.fcol ul{list-style:none;margin-top:14px}
.fcol li{font-size:12px;line-height:25px}
.fcol li::before{content:"•";margin-right:8px}
.vline{position:absolute;top:40px;width:1px;height:200px;background:#4b4787}
.contact-row{display:flex;gap:10px;font-size:12px;line-height:17px;margin-top:22px;width:280px}
.inquiry input,.inquiry textarea{display:block;width:243px;border:none;background:var(--white);font-family:"Lato",Arial,sans-serif;font-size:12px;color:#333;padding:4px 6px;margin-top:6px}
.inquiry input{height:25px}
.inquiry textarea{height:45px;resize:none}
.submit{display:inline-block;margin-top:8px;background:var(--sky);color:var(--white);font-weight:700;font-size:17px;padding:4px 18px;border:1.5px solid #8fd6f7}
.footer-brand{position:absolute;left:960px;top:48px;width:190px;text-align:center}
.footer-brand span{display:block;width:120px;height:120px;border-radius:50%;background:var(--sky);margin:0 auto}
.footer-brand p{font-family:"Cinzel",Georgia,serif;font-weight:700;font-size:20px;margin-top:14px;color:var(--white)}
.bottombar{position:absolute;top:2660px;left:0;width:1200px;height:43px;background:var(--sky)}
.bottombar p{position:absolute;left:99px;top:13px;font-size:13px;color:var(--navy);font-weight:700}
.bottombar .socials{position:absolute;right:87px;top:6px;display:flex;gap:8px}
.bottombar .social{background:var(--navy)}
</style>
</head>
<body>

<header class="hero">
  <div class="brand"><span class="brand-dot"></span><span class="brand-name">Qu-Tessaroly</span></div>
  <div class="topbar">
    <span class="phone">
      <svg width="26" height="26" viewBox="0 0 26 26"><circle cx="13" cy="13" r="12" fill="none" stroke="#24205e" stroke-width="2"/><path d="M9 7l3 3-2 2c1 2 2 3 4 4l2-2 3 3-2 2c-5 0-10-5-10-10z" fill="#24205e"/></svg>
      +64 21 555 0148
    </span>
    <span class="social"></span><span class="social"></span><span class="social"></span>
  </div>
  <ul class="nav">
    <li class="active">Home</li><li>Shop</li><li>Our Purpose</li><li>What We Do</li><li>The Team</li><li>Contact Us</li>
  </ul>
  <div class="book" role="img" aria-label="Photo of an open blank notebook"></div>
  <div class="hero-copy">
    <h1>Need a breakthrough<br>innovation, but staring at<br>a blank piece of paper?</h1>
    <span class="btn-buy-hero">BUY NOW</span>
    <p class="offer">‘The Ninja’<br>3 Hours of Intensive Support</p>
  </div>
  <div class="dots"><span></span><span></span><span></span><span></span></div>
</header>

<section class="welcome">
  <h2><i></i>Welcome to <em>Qu-Tessaroly</em></h2>
  <p>Lorem ipsum dolor sit amet, consectetuer adipiscing elit, sed diam nonummy nibh euismod tincidunt ut laoreet dolore magna aliquam erat volutpat. Ut wisi enim ad minim veniam, quis nostrud exerci tation ullamcorper suscipit lobortis nisl ut aliquip ex ea commodo consequat. Duis autem vel eum iriure dolor in hendrerit in vulputate velit esse molestie consequat, vel illum dolore eu feugiat nulla facilisis at vero eros et accumsan et iusto odio dignissim qui blandit praesent luptatum zzril delenit augue duis dolore te feugait nulla facilisi.</p>
  <span class="btn-outline">READ MORE</span>
</section>

<section class="features">
  <div class="feature feature-what">
    <svg width="72" height="90" viewBox="0 0 72 90"><circle cx="36" cy="9" r="8" fill="#24205e"/><rect x="26" y="20" width="20" height="34" rx="4" fill="#24205e"/><ellipse cx="36" cy="70" rx="32" ry="14" fill="none" stroke="#24205e" stroke-width="6"/><rect x="30" y="50" width="12" height="20" fill="#24205e"/></svg>
    <h3>What We Do</h3>
    <p class="lead">We innovate. For you<br>The most common things we hear are:</p>
    <ul>
      <li>I need a breakthrough innovation, but am staring at a blank piece of paper</li>
      <li>I have to come up with a great idea, but have a limited budget and little time</li>
    </ul>
    <span class="btn-outline">READ MORE</span>
  </div>
  <div class="feature feature-purpose">
    <svg width="112" height="90" viewBox="0 0 112 90"><rect x="36" y="22" width="40" height="56" rx="4" fill="#24205e"/><g fill="#24205e"><circle cx="56" cy="10" r="8"/><circle cx="22" cy="30" r="8"/><circle cx="90" cy="30" r="8"/><circle cx="16" cy="54" r="8"/><circle cx="96" cy="54" r="8"/><circle cx="22" cy="78" r="8"/><circle cx="90" cy="78" r="8"/></g></svg>
    <h3>Our Purpose</h3>
    <p class="lead">Our purpose is to re-define how companies like yours get great innovation. Quickly.</p>
    <p class="body">The team at Qu-Tessaroly have worked both client side and as consultants. We know what works and how things tick...</p>
    <span class="btn-outline">READ MORE</span>
  </div>
</section>

<section class="how">
  <h2 class="section-title">How It Works</h2>
  <svg class="divider" viewBox="0 0 376 20"><line x1="0" y1="10" x2="376" y2="10" stroke="#cfd3dc" stroke-width="2"/><rect x="160" y="2" width="56" height="6" rx="3" fill="#5cc6f2"/><rect x="166" y="12" width="44" height="6" rx="3" fill="#1ea8e8"/></svg>
  <svg class="steps" width="1200" height="300" viewBox="0 0 1200 300">
    <path d="M310 70 Q456 110 602 70 Q748 110 888 70 L888 230 Q748 190 602 230 Q456 190 310 230 Z" fill="#3fb6ef"/>
    <circle cx="310" cy="150" r="121" fill="#fff" stroke="#1ea8e8" stroke-width="10"/>
    <circle cx="602" cy="150" r="121" fill="#fff" stroke="#35b1ec" stroke-width="10"/>
    <circle cx="888" cy="150" r="121" fill="#fff" stroke="#6fcdf4" stroke-width="10"/>
    <path d="M442 136 l16 14 -16 14z M734 136 l16 14 -16 14z" fill="#fff"/>
    <g fill="#1ea8e8">
      <circle cx="310" cy="85" r="20"/><rect x="300" y="104" width="20" height="12" rx="2"/>
      <path d="M280 80h-12M340 80h12M288 60l-8-8M332 60l8-8M310 52v-12" stroke="#1ea8e8" stroke-width="3"/>
      <circle cx="602" cy="70" r="18" fill="none" stroke="#1ea8e8" stroke-width="3"/>
      <rect x="596" y="66" width="12" height="34" rx="6"/><rect x="596" y="86" width="30" height="26" rx="8"/>
      <circle cx="876" cy="62" r="9"/><rect x="868" y="74" width="16" height="26" rx="3"/><rect x="884" y="80" width="36" height="5"/><rect x="902" y="85" width="5" height="28"/><rect x="862" y="100" width="22" height="5"/><rect x="866" y="105" width="5" height="12"/>
    </g>
  </svg>
  <p class="step-label" style="left:210px;top:297px">Shop Through Our Innovation Window</p>
  <p class="step-label" style="left:502px;top:297px">Select the Product</p>
  <p class="step-label" style="left:788px;top:297px">We Start Working</p>
</section>

<section class="shop">
  <h2 class="section-title">Innovation Shop</h2>
  <svg class="divider" viewBox="0 0 376 20"><line x1="0" y1="10" x2="376" y2="10" stroke="#b8c0d4" stroke-width="2"/><rect x="160" y="2" width="56" height="6" rx="3" fill="#5cc6f2"/><rect x="166" y="12" width="44" height="6" rx="3" fill="#1ea8e8"/></svg>
  <div class="product" style="left:120px"><div class="product-icon"><span></span></div><h4>The ‘Barista’</h4><p class="price">$ FREE</p><span class="btn-buy">BUY NOW</span></div>
  <div class="product" style="left:374px"><div class="product-icon"><span></span></div><h4>The ‘Sentinel’</h4><p class="price">$ 499</p><span class="btn-buy">BUY NOW</span></div>
  <div class="product" style="left:635px"><div class="product-icon"><span></span></div><h4>The ‘Ninja’</h4><p class="price">$ 749</p><span class="btn-buy">BUY NOW</span></div>
  <div class="product" style="left:889px"><div class="product-icon"><span></span></div><h4>‘The Maverick’</h4><p class="price featured">$ 949</p><span class="btn-buy">BUY NOW</span></div>
</section>

<footer class="footer">
  <div class="fcol" style="left:99px">
    <h5>Quick Links</h5>
    <ul><li>Home</li><li>Shop</li><li>Our Purpose</li><li>What We Do</li><li>The Team</li><li>Contact Us</li></ul>
  </div>
  <div class="vline" style="left:263px"></div>
  <div class="fcol" style="left:310px">
    <h5 style="border:none">Contact Details</h5>
    <div class="contact-row"><svg width="12" height="16" viewBox="0 0 12 16"><path d="M6 0a6 6 0 0 1 6 6c0 4-6 10-6 10S0 10 0 6a6 6 0 0 1 6-6z" fill="#fff"/><circle cx="6" cy="6" r="2.2" fill="#24205e"/></svg><span>12 Kowhai Lane, Palm Beach, Waiheke Island, Auckland, New Zealand</span></div>
    <div class="contact-row" style="margin-top:26px"><svg width="14" height="14" viewBox="0 0 26 26"><path d="M6 2l5 5-3 3c2 4 4 6 8 8l3-3 5 5-4 4C11 24 2 15 2 6z" fill="#fff"/></svg><span>+64 21 555 0148</span></div>
    <div class="contact-row" style="margin-top:26px"><svg width="14" height="12" viewBox="0 0 14 12"><rect width="14" height="12" rx="1" fill="#fff"/><path d="M0 1l7 6 7-6" fill="none" stroke="#24205e" stroke-width="1.4"/></svg><span>contact@qu-tessaroly.com</span></div>
  </div>
  <div class="vline" style="left:590px"></div>
  <div class="fcol inquiry" style="left:645px">
    <h5 style="border:none">Quick Inquiry</h5>
    <input type="text" value="Your Name">
    <input type="text" value="Email">
    <textarea>Message</textarea>
    <span class="submit">SUBMIT</span>
  </div>
  <div class="vline" style="left:945px"></div>
  <div class="footer-brand"><span></span><p>Qu-Tessaroly</p></div>
</footer>

<div class="bottombar">
  <p>Copyright © 2016 Qu-Tessaroly. All Rights Reserved.</p>
  <div class="socials"><span class="social"></span><span class="social"></span><span class="social"></span></div>
</div>

</body>
</html>
```